Business Card Design Project

We need a business card for a chiropractic and rehabilitation center. We already have a logo and need the card to follow the color and feel of the logo.

Target Market(s)

adults 30-55 that have some ache or pain that is interfering with their life, so much as they are ready to do something about it.

Industry/Entity Type

Business

```html
<!DOCTYPE html>
<html lang="en">
<head>
<meta charset="utf-8">
<title>Northgate Spine &amp; Rehab — Business Card</title>
<link rel="stylesheet" href="https://fonts.googleapis.com/css2?family=Source+Sans+3:ital,wght@0,400;0,600;0,700;1,700&display=swap">
<style>
  :root {
    --backdrop: #2b3434;
    --card: #ffffff;
    --ink: #333333;
    --brand-grey: #58595b;
    --brand-orange: #f7941d;
  }
  * { margin: 0; padding: 0; box-sizing: border-box; }
  html, body {
    width: 987px;
    height: 1200px;
    overflow: hidden;
    background: var(--backdrop);
    font-family: "Source Sans 3", "Myriad Pro", Arial, sans-serif;
    color: var(--ink);
  }
  .sheet { position: relative; width: 987px; height: 1200px; }
  .card {
    position: absolute;
    width: 790px;
    height: 450px;
    background: var(--card);
    border-radius: 30px;
    text-align: center;
  }
  .card--front { left: 93px; top: 108px; }
  .card--back { left: 92px; top: 637px; }

  .brand {
    position: absolute;
    left: 0; right: 0;
    display: flex;
    justify-content: center;
    align-items: center;
    gap: 16px;
  }
  .card--front .brand { top: 90px; }
  .card--back .brand { top: 130px; }
  .brand__name {
    font-weight: 600;
    font-size: 50px;
    letter-spacing: 1px;
    color: var(--brand-grey);
    line-height: 1;
  }
  .brand__dot {
    width: 30px; height: 30px;
    border-radius: 50%;
    background: var(--brand-orange);
  }

  .holder {
    position: absolute;
    top: 276px; left: 0; right: 0;
    font-size: 21px;
  }
  .holder__name { font-weight: 700; font-size: 25px; }

  .contact {
    position: absolute;
    top: 340px; left: 0; right: 0;
    font-size: 20px;
    line-height: 32px;
  }
  .contact__label { font-weight: 700; font-style: italic; }
  .contact__sep { margin: 0 6px; }

  .web {
    position: absolute;
    top: 355px; left: 0; right: 0;
    font-size: 35px;
    color: var(--ink);
  }
</style>
</head>
<body>
<main class="sheet">
  <section class="card card--front">
    <div class="brand">
      <span class="brand__name">NORTHGATE REHAB</span>
      <span class="brand__dot"></span>
    </div>
    <p class="holder"><span class="holder__name">Your Name</span>, Designation</p>
    <div class="contact">
      <p><span class="contact__label">t</span> : 123-123-1234 <span class="contact__sep">|</span> <span class="contact__label">c</span> : 123-123-1234</p>
      <p><span class="contact__label">e</span> : info@website.com <span class="contact__sep">|</span> <span class="contact__label">w</span> : www.website.com</p>
      <p>123 Street, Suit #123, Your City, State 12345</p>
    </div>
  </section>

  <section class="card card--back">
    <div class="brand">
      <span class="brand__name">NORTHGATE REHAB</span>
      <span class="brand__dot"></span>
    </div>
    <p class="web">www.website.com</p>
  </section>
</main>
</body>
</html>
```